Invitation Design Project

In May 2014, my husband and I celebrate our 10th wedding anniversary, and in June 2014 I celebrate my 40th birthday. We will be having a "10/40" party in June 2014 for both events.

This party will be held on my property, "Hollowmere Farm" in North Queensland, so the invitation needs to be fun, whimsical and reflective of both our farm and the Australian bush. You can see photos of our property on facebook: https://www.pagebook.example/hollowmerefarm

The party will be held on 7 June 2014, RSVP by 1 April 2014.

Target Market(s)

Our family and friends - all ages and backgrounds

Industry/Entity Type

Wedding

Requirements
Must have
• Must have the following details: (wording is flexible)
- Mirla & Tobias celebrate their 10th wedding anniversary on 8 May 2014.
- Mirla turns 40 on 9 June 2014
- Party to be held on Hollowmere Farm, 6pm start. Dinner, entertainment and courtesy bus provided, BYO drinks.
- RSVP by 1 April 2014
Must have correct spelling and grammar on the first draft please.
Nice to have
• It might be fun if the invitation could include our pets (dogs, cats, goats, pigs, chickens, parrakeet - see pictures on the facebook link above) in some way, in cartoon form in the background maybe?
Should not have
• I'm not particularly interested in having our photos incorporated into the invitation.

```html
<!DOCTYPE html>
<html lang="en">
<head>
<meta charset="utf-8">
<title>Mirla and Tobias – 10/40 Party Invitation</title>
<link rel="stylesheet" href="https://fonts.googleapis.com/css2?family=Great+Vibes&family=Crimson+Text:ital@0;1&display=swap">
<style>
  :root {
    --paper: #ffffff;
    --script-red: #c2121f;
    --leaf-green: #5b7c3a;
    --grass-light: #d3ec8e;
    --grass-mid: #a9d65c;
  }
  * { margin: 0; padding: 0; box-sizing: border-box; }
  html, body {
    width: 848px;
    height: 1200px;
    overflow: hidden;
    background: var(--paper);
  }
  .invitation {
    position: relative;
    width: 848px;
    height: 1200px;
    background: var(--paper);
    font-family: "Crimson Text", "Goudy Old Style", serif;
    font-variant-numeric: lining-nums;
    color: var(--leaf-green);
  }
  .hosts { font-weight: 400; }
  .script {
    font-family: "Great Vibes", cursive;
    color: var(--script-red);
    font-weight: 400;
  }
  .host {
    position: absolute;
    font-size: 96px;
    line-height: 1;
  }
  .host--first { left: 102px; top: 52px; }
  .host--second { left: 432px; top: 104px; }
  .host-joiner {
    position: absolute;
    left: 345px;
    top: 122px;
    font-size: 28px;
    font-weight: 400;
    letter-spacing: 0.5px;
  }
  .line {
    position: absolute;
    left: 0;
    width: 100%;
    text-align: center;
    font-size: 24px;
    line-height: 1;
    white-space: nowrap;
  }
  .line--shift { left: -36px; }
  .line .script { font-size: 38px; }
  .line--small { font-size: 22px; }
  .line--italic { font-style: italic; font-size: 26px; }
  .rsvp {
    position: absolute;
    left: 574px;
    top: 848px;
    font-size: 26px;
    line-height: 35px;
  }
  .farm-scene {
    position: absolute;
    left: 45px;
    top: 850px;
    width: 745px;
    height: 300px;
  }
</style>
</head>
<body>
<main class="invitation">
  <h1 class="hosts">
    <span class="host host--first script">Mirla</span>
    <span class="host-joiner">AND</span>
    <span class="host host--second script">Tobias</span>
  </h1>

  <p class="line" style="top:263px">INVITE YOU TO SHARE IN THEIR</p>
  <p class="line" style="top:295px">a “10/40” PARTY&nbsp; CELEBRATION</p>

  <p class="line" style="top:353px">OUR 10th WEDDING ANNIVERSARY CELEBRATION</p>
  <p class="line" style="top:391px">8th MAY 2014</p>

  <p class="line line--shift" style="top:461px"><span class="script">Mirla</span> TURNS 40 CELEBRATION</p>
  <p class="line" style="top:506px">9th JUNE 2014</p>

  <p class="line line--small" style="top:582px">VENUE IS</p>
  <p class="line line--small" style="top:607px">OUR “Hollowmere Farm”</p>

  <p class="line" style="top:659px">7th JUNE 2014</p>
  <p class="line" style="top:693px">START AT SIX O’CLOCK IN THE AFTERNOON</p>
  <p class="line line--italic" style="top:722px">Dinner, entertainment and courtesy bus provided, BYO drinks.</p>

  <svg class="farm-scene" viewBox="0 0 745 300" role="img" aria-label="Cartoon farm animals: two white hens, a white cat and yellow chicks with eggs in straw nests on green grass">
    <defs>
      <radialGradient id="grassTone" cx="50%" cy="70%" r="65%">
        <stop offset="0%" stop-color="var(--grass-mid)"/>
        <stop offset="100%" stop-color="var(--grass-light)"/>
      </radialGradient>
    </defs>
    <path d="M0 285 C30 250 90 215 150 170 C170 90 250 60 330 50 C400 10 470 30 520 60 C580 110 640 170 690 200 C720 230 740 260 745 290 L745 300 L0 300 Z" fill="url(#grassTone)"/>
  </svg>

  <p class="rsvp">RSVP by<br>1st APRIL 2014<br>phone number</p>
</main>
</body>
</html>
```